Meadowlark Crest Nutraceutical Website

Need a website for a vitamin gummy manufacturing and white-labeling company based in Charleston, SC. We service Quillmarket brands, Ecommerce brands, and any customer needing supplement gummies white labeled. I added out logos for color and style. We have always used navy blue, gold, and white in our color palet, we decided to add purple into the logo.

Our partner's website, that makes caples and powders, is https://www.bravolithworks.com/

We are just now moving into our facility and don't have pictures or videos of the space, equipement, products, etc. I attached the flyer for the machine we have as reference.

The site just needs to be a simple landing page for now. 'Request Quote' for sales leads and 'enquire here' for job applications. I just need a simple site so we can have our state's dept of commerce announce us publicly.

There are 2 logos. We will be using 'Meadowlark Crest Nutraceutical' for now. I cannot use "MC Nutra" until I have approval from our state, but "MC nutra" will be the end logo for use after a couple of months.

```html
<!DOCTYPE html>
<html lang="en">
<head>
<meta charset="utf-8">
<title>Meadowlark Crest Nutraceutical — White Label Vitamin Gummies Manufacturers</title>
<link rel="stylesheet" href="https://fonts.googleapis.com/css2?family=Montserrat:wght@400;500;600;700;800&display=swap">
<style>
:root{
  --navy:#253a6c;
  --navy-dark:#1f3263;
  --sky:#a9dbef;
  --sky-text:#8fd3ee;
  --ice:#eaf3fa;
  --ink:#222;
  --muted:#5a6a86;
  --white:#fff;
  --card:#f3f4f6;
}
*{box-sizing:border-box;margin:0;padding:0}
html,body{width:1200px;height:4138px;overflow:hidden}
body{font-family:"Montserrat",sans-serif;color:var(--ink);background:var(--white);position:relative}
.btn{position:absolute;display:flex;align-items:center;justify-content:center;font-size:13px;font-weight:500}
.btn-sky{background:var(--sky);color:var(--navy)}
.btn-navy{background:var(--navy);color:var(--white)}
.btn-pill{border-radius:16px}

/* header */
.site-header{position:absolute;left:0;top:0;width:1200px;height:75px;background:var(--white)}
.brand{position:absolute;left:146px;top:24px;line-height:1}
.brand-name{font-size:21px;font-weight:600;letter-spacing:2px;color:var(--navy)}
.brand-sub{font-size:14px;letter-spacing:2.5px;color:#7fb8d8;margin-top:4px;padding-left:38px}
.call{position:absolute;left:780px;top:12px;display:flex;align-items:center;gap:8px;color:var(--navy)}
.call small{display:block;font-size:11px}
.call strong{font-size:15px;font-weight:500}

/* hero */
.hero{position:absolute;left:0;top:75px;width:1200px;height:576px;background:linear-gradient(90deg,#eef4f8 0%,#e3eef6 50%,#d5e8f3 100%)}
.hero-photo{position:absolute;left:640px;top:0;width:560px;height:576px;background:radial-gradient(ellipse at 60% 50%,#f0b86a 0%,#e98aa0 25%,#cfe3ee 60%,rgba(213,232,243,0) 80%)}
.hero-box{position:absolute;left:140px;top:184px;width:520px;height:233px;background:var(--white);border-left:7px solid var(--navy);padding:14px 0 0 22px}
.hero-kicker{font-size:21px;font-weight:700;color:var(--ink)}
.hero-title{font-size:37px;font-weight:800;color:var(--navy);margin-top:4px;letter-spacing:-.3px}
.hero-text{font-size:14.5px;line-height:28px;margin-top:6px}

/* intro */
.section-title{position:absolute;left:0;width:1200px;text-align:center;font-size:33px;font-weight:700;color:var(--navy)}
.intro-sub{position:absolute;left:0;top:761px;width:1200px;text-align:center;font-size:13px;color:var(--sky-text);text-decoration:underline}
.lead{position:absolute;left:205px;width:790px;text-align:center;font-size:12.5px;line-height:22px}
.feature{position:absolute;top:977px;width:213px;height:191px;background:var(--card);text-align:center}
.feature.active{background:#f4f8fb;border:2px solid #c9e3f1}
.feature svg{margin-top:25px}
.feature p{font-size:21px;font-weight:500;color:var(--navy);margin-top:6px}

/* service */
.service{position:absolute;left:0;top:1253px;width:1200px;height:734px;background:radial-gradient(ellipse at 30% 30%,#7a2a2a 0%,#3d0f18 45%,#5a2020 80%,#2a0a10 100%)}
.service-photo{position:absolute;left:141px;top:85px;width:506px;height:564px;background:linear-gradient(160deg,#dfe6ec 0%,#a9b6c2 45%,#4f5d6e 100%)}
.service-title{position:absolute;left:719px;top:80px;font-size:32px;font-weight:700;color:var(--sky-text)}
.service-item{position:absolute;left:719px;width:340px;color:var(--white)}
.service-head{display:flex;align-items:center;gap:12px;font-size:16.5px;color:var(--sky-text)}
.service-head .dot{width:41px;height:41px;border-radius:50%;background:var(--white);flex:none;display:flex;align-items:center;justify-content:center}
.service-item p{font-size:12.5px;line-height:22px;margin-top:19px}

/* plant */
.plant-img{position:absolute;top:2124px;width:297px;height:254px}
.arrow{position:absolute;top:2234px;width:36px;height:36px;border-radius:50%;display:flex;align-items:center;justify-content:center}
.candy-deco{position:absolute;left:900px;top:2360px;width:300px;height:166px;background:radial-gradient(ellipse at 65% 70%,#f7a33b 0%,#f5c978 30%,rgba(255,255,255,0) 70%)}

/* third party */
.third{position:absolute;left:0;top:2526px;width:1200px;height:521px;background:var(--ice)}
.third h2{position:absolute;left:141px;top:90px;font-size:33px;font-weight:700;color:var(--navy);line-height:38px}
.third .copy{position:absolute;left:141px;top:174px;width:385px;font-size:12.5px;line-height:22px}
.third .copy p+p{margin-top:8px}
.third-photo{position:absolute;left:614px;top:85px;width:445px;height:353px;background:linear-gradient(135deg,#c8b39a 0%,#7d6d5e 45%,#2f3e4a 100%)}

/* why */
.stat{position:absolute;top:3285px;width:169px;height:167px;background:var(--white);box-shadow:0 2px 10px rgba(0,0,0,.09);text-align:center}
.stat svg{margin-top:26px}
.stat .num{font-size:23px;font-weight:500;color:var(--navy);margin-top:4px}
.stat .num sup{color:var(--sky-text);font-size:16px;vertical-align:0}
.stat .label{font-size:15px;font-weight:500;margin-top:4px}

/* footer */
.footer{position:absolute;left:0;top:3745px;width:1200px;height:393px;background:var(--navy)}
.job{position:absolute;left:229px;top:3537px;width:742px;height:280px;background:linear-gradient(90deg,#f4f0e8 0%,#efe9df 50%,#e7ddcf 100%)}
.job-photo{position:absolute;left:470px;top:0;width:272px;height:280px;background:linear-gradient(150deg,#eef0ec 0%,#c6c9c2 45%,#34404c 100%)}
.job h2{position:absolute;left:30px;top:58px;font-size:32px;font-weight:700;color:var(--navy)}
.job p{position:absolute;left:30px;top:108px;width:345px;font-size:12.5px;line-height:22px}
.job-candy{position:absolute;left:20px;top:225px;width:170px;height:55px;background:radial-gradient(ellipse,#f06a5a 0%,#f7b84a 45%,rgba(239,233,223,0) 75%)}
.footer-brand{position:absolute;left:0;top:132px;width:1200px;text-align:center;color:var(--white);line-height:1}
.footer-brand .a{font-size:36px;font-weight:500;letter-spacing:3px}
.footer-brand .b{font-size:26px;letter-spacing:3px;margin-top:8px;font-weight:400}
.footer-rule{position:absolute;left:141px;top:230px;width:918px;height:1px;background:rgba(255,255,255,.15)}
.contact{position:absolute;top:266px;display:flex;align-items:center;gap:14px;color:var(--white);font-size:13.5px;line-height:22px}
.contact .ic{width:42px;height:42px;border-radius:50%;background:var(--white);display:flex;align-items:center;justify-content:center}
.vsep{position:absolute;top:262px;width:1px;height:50px;background:rgba(255,255,255,.2)}
.copyright{position:absolute;left:141px;top:360px;font-size:12px;color:var(--white)}
.social{position:absolute;top:355px;width:24px;height:24px;border:1.5px solid var(--white);border-radius:50%}
</style>
</head>
<body>

<header class="site-header">
  <div class="brand"><div class="brand-name">MEADOWLARK CREST</div><div class="brand-sub">NUTRACEUTICAL</div></div>
  <div class="call">
    <svg width="22" height="22" viewBox="0 0 24 24" fill="none" stroke="#9ac4dd" stroke-width="1.6"><path d="M5 3h4l2 5-2.5 1.5a11 11 0 0 0 6 6L16 13l5 2v4a2 2 0 0 1-2 2A16 16 0 0 1 3 5a2 2 0 0 1 2-2z"/></svg>
    <div><small>Call Us</small><strong>+123 456 7890</strong></div>
  </div>
  <div class="btn btn-navy btn-pill" style="left:933px;top:20px;width:120px;height:30px;font-size:12px">Get A Quote</div>
</header>

<section class="hero">
  <div class="hero-photo" role="img" aria-label="Jar spilling colourful vitamin gummies in a bright factory"></div>
  <div class="hero-box">
    <div class="hero-kicker">Leading white Label Vitamin</div>
    <h1 class="hero-title">Gummies Manufacturers</h1>
    <p class="hero-text">Verified Private Label Vitamin Gummies Manufacturers.<br>Take Your Supplement Brand To The Next Level.</p>
  </div>
  <div class="btn btn-navy btn-pill" style="left:167px;top:355px;width:120px;height:30px;font-size:12px">Get A Quote</div>
</section>

<section class="intro">
  <h2 class="section-title" style="top:715px">Introducing Meadowlark Crest</h2>
  <div class="intro-sub">PREMIUM VITAMIN GUMMIES</div>
  <p class="lead" style="top:792px">Lorem ipsum dolor sit amet consectmet consectetur adipiscing elit. Mauris at ante quis nunc faucibus ullamcorper sedt eget ipsum. In congue vietur adipiscing elit. Mauris at ante quis nunc faucibus ullamcorper sedt eget ipsum. In congue vitae augue aliquet consectetur. In a auctor arcu vel venenatis orci. Donec fringilla turpis id nisi pellentesque fringilla. Nullam quis lectus id risus ultricies pharetra euismod sed massa.</p>
  <div class="btn btn-sky" style="left:533px;top:898px;width:134px;height:34px">Request Quote</div>

  <div class="feature" style="left:140px">
    <svg width="86" height="86" viewBox="0 0 86 86" fill="none" stroke="#253a6c" stroke-width="2.5"><circle cx="43" cy="43" r="40"/><circle cx="43" cy="43" r="33"/><path d="M30 60c0-16 10-26 28-28-2 18-12 26-28 28z"/><path d="M30 60l18-18"/></svg>
    <p>Vegan</p>
  </div>
  <div class="feature" style="left:375px">
    <svg width="86" height="86" viewBox="0 0 86 86" fill="none" stroke="#253a6c" stroke-width="2.5"><circle cx="43" cy="43" r="40"/><circle cx="43" cy="43" r="33"/><path d="M20 66L66 20"/><text x="43" y="50" text-anchor="middle" font-family="Montserrat,sans-serif" font-size="19" fill="none" stroke="#253a6c" stroke-width="1.3">GMO</text></svg>
    <p>Non-GMO</p>
  </div>
  <div class="feature" style="left:611px">
    <svg width="86" height="86" viewBox="0 0 86 86" fill="none" stroke="#253a6c" stroke-width="2.5"><circle cx="43" cy="43" r="40"/><circle cx="43" cy="43" r="33"/><path d="M20 66L66 20"/><path d="M43 66V24M43 34c-6-2-8-6-8-10M43 34c6-2 8-6 8-10M43 46c-6-2-8-6-8-10M43 46c6-2 8-6 8-10"/></svg>
    <p>Gluten Free</p>
  </div>
  <div class="feature active" style="left:847px">
    <svg width="86" height="86" viewBox="0 0 86 86" fill="none" stroke="#253a6c" stroke-width="2.5"><circle cx="43" cy="43" r="40"/><circle cx="43" cy="43" r="33"/><path d="M20 66L66 20"/><ellipse cx="45" cy="48" rx="13" ry="10"/><circle cx="36" cy="36" r="6"/><path d="M33 30l-2-8M38 30l2-8"/></svg>
    <p>Cruelty Free</p>
  </div>
</section>

<section class="service">
  <div class="service-photo" role="img" aria-label="Two business partners shaking hands in an office"></div>
  <h2 class="service-title">We Service</h2>
  <div class="service-item" style="top:142px">
    <div class="service-head"><span class="dot"></span>Quillmarket Brands</div>
    <p>Lorem ipsum dolor sit amet, consectetur adipiscing elit. Mauris at ante quis nunc faucibus ullamcorper sed eget ipsum vitae augue aliquet.</p>
  </div>
  <div class="service-item" style="top:302px">
    <div class="service-head"><span class="dot"><svg width="20" height="20" viewBox="0 0 24 24" fill="none" stroke="#253a6c" stroke-width="1.8"><path d="M3 4h3l2 11h11l2-8H7"/><circle cx="10" cy="19" r="1.5"/><circle cx="17" cy="19" r="1.5"/></svg></span>Ecommerce Brands</div>
    <p>Lorem ipsum dolor sit amet, consectetur adipiscing elit. Mauris at ante quis nunc faucibus ullamcorper sed eget ipsum vitae augue aliquet.</p>
  </div>
  <div class="service-item" style="top:455px">
    <div class="service-head"><span class="dot"><svg width="20" height="20" viewBox="0 0 24 24" fill="none" stroke="#253a6c" stroke-width="1.6"><circle cx="8" cy="14" r="4"/><circle cx="15" cy="9" r="4"/><circle cx="16" cy="17" r="3"/></svg></span><span>Customer Needing<br>Supplement Gummies</span></div>
    <p style="margin-top:12px">Lorem ipsum dolor sit amet, consectetur adipiscing elit. Mauris at ante quis nunc faucibus ullamcorper sed eget ipsum vitae augue aliquet.</p>
  </div>
  <div class="btn btn-sky" style="left:719px;top:614px;width:134px;height:33px">Request Quote</div>
</section>

<section class="plant">
  <h2 class="section-title" style="top:2063px">Manufacturing Plant Images</h2>
  <div class="plant-img" style="left:141px;background:linear-gradient(135deg,#e7ecef,#a9b5bd)" role="img" aria-label="Technician in protective gear beside steel mixing tanks"></div>
  <div class="plant-img" style="left:451px;background:linear-gradient(135deg,#dfe5ea,#8a969f)" role="img" aria-label="Row of stainless steel processing vessels"></div>
  <div class="plant-img" style="left:762px;background:linear-gradient(135deg,#eef0f1,#b8bec2)" role="img" aria-label="Clean room with gummy production machine"></div>
  <div class="arrow" style="left:87px;border:1.5px solid #a9dbef">
    <svg width="16" height="16" viewBox="0 0 16 16" fill="none" stroke="#a9dbef" stroke-width="1.6"><path d="M13 8H3M7 4L3 8l4 4"/></svg>
  </div>
  <div class="arrow" style="left:1076px;background:var(--navy)">
    <svg width="16" height="16" viewBox="0 0 16 16" fill="none" stroke="#fff" stroke-width="1.8"><path d="M3 8h10M9 4l4 4-4 4"/></svg>
  </div>
  <div class="candy-deco" role="img" aria-label="Glass jar of orange and yellow gummies"></div>
  <div class="btn btn-sky" style="left:533px;top:2408px;width:134px;height:33px">Request Quote</div>
</section>

<section class="third">
  <h2>Third Party Gummies<br>Manufacturing</h2>
  <div class="copy">
    <p>Lorem ipsum dolor sit amet, consectetur adipiscing elit. Mauris at ante quis nunc faucibus ullamcorper sed eget ipsum. In congue vitae augue aliquet consectetur. In a auctor arcu, vel venenatis orci. Donec fringilla turpis id nisi pellentesque fringilla.</p>
    <p>In congue vitae augue aliquet consectetur. In a auctor arcuvel veneatis orci. Donec frinilla turpis nisi pellentesque fringilla. Nullam quis lectus id risus ultricies pharetra euismod sed massa.</p>
  </div>
  <div class="btn btn-navy" style="left:141px;top:394px;width:135px;height:33px">Request Quote</div>
  <div class="third-photo" role="img" aria-label="Business team shaking hands across a meeting table"></div>
</section>

<section class="why">
  <h2 class="section-title" style="top:3123px">Why Choose Us</h2>
  <p class="lead" style="left:160px;width:880px;top:3176px">Meadowlark Crest Nutraceutical  being a reputed third party manufactuer for gummies offers the products that are rich in essential nutritions with the elements like vitamins, calcium, iron, glutathione, zinc or any other essential mineral as per the needs for the body. With our multivitamin and nutritious gummies we have made a great reputation in the market, here are some of the points that you should consider to collaborate with us.</p>

  <div class="stat" style="left:141px">
    <svg width="56" height="46" viewBox="0 0 56 46" fill="none" stroke="#253a6c" stroke-width="2"><circle cx="28" cy="12" r="8"/><path d="M14 42c0-9 6-15 14-15s14 6 14 15z"/><circle cx="12" cy="20" r="5"/><circle cx="44" cy="20" r="5"/><path d="M2 40c0-6 4-10 9-10M54 40c0-6-4-10-9-10"/></svg>
    <div class="num">1500<sup>+</sup></div><div class="label">Satisfied Clients</div>
  </div>
  <div class="stat" style="left:329px">
    <svg width="56" height="46" viewBox="0 0 56 46" fill="none" stroke="#253a6c" stroke-width="2"><path d="M18 6l10-4 10 4v12l-10 4-10-4z"/><path d="M18 6l10 4 10-4M28 10v12"/><path d="M4 20l8 20h10M52 20l-8 20H34"/></svg>
    <div class="num">500<sup>+</sup></div><div class="label">Products</div>
  </div>
  <div class="stat" style="left:516px">
    <svg width="56" height="50" viewBox="0 0 56 50" fill="none" stroke="#253a6c" stroke-width="2"><circle cx="28" cy="10" r="6"/><circle cx="15" cy="16" r="5"/><circle cx="41" cy="16" r="5"/><path d="M18 46V28a10 10 0 0 1 20 0v18M6 46V30a9 9 0 0 1 9-8M50 46V30a9 9 0 0 0-9-8M4 46h48"/></svg>
    <div class="num">25<sup>+</sup></div><div class="label">Employees</div>
  </div>
  <div class="stat" style="left:703px">
    <svg width="56" height="46" viewBox="0 0 56 46" fill="none" stroke="#253a6c" stroke-width="2"><path d="M18 4h20v10a10 10 0 0 1-20 0z"/><path d="M18 8H10c0 8 4 12 9 12M38 8h8c0 8-4 12-9 12"/><path d="M28 24v10M20 42h16l-2-8H22z"/><path d="M28 8l2 4h4l-3 3 1 4-4-2-4 2 1-4-3-3h4z"/></svg>
    <div class="num">25<sup>+</sup></div><div class="label">Awards</div>
  </div>
  <div class="stat" style="left:890px">
    <svg width="56" height="46" viewBox="0 0 56 46" fill="none" stroke="#253a6c" stroke-width="2"><path d="M4 44h48M8 44V22l12-8v8l12-8v8l12-8V44M44 14V2h6v42"/><rect x="14" y="30" width="6" height="6"/><rect x="26" y="30" width="6" height="6"/><rect x="38" y="30" width="6" height="6"/></svg>
    <div class="num">3<sup>+</sup></div><div class="label">Mfg. Units</div>
  </div>
</section>

<footer class="footer">
  <div class="footer-brand"><div class="a">MEADOWLARK CREST</div><div class="b">NUTRACEUTICAL</div></div>
  <div class="footer-rule"></div>
  <div class="contact" style="left:168px">
    <span class="ic"><svg width="18" height="18" viewBox="0 0 24 24" fill="#253a6c"><path d="M12 2a7 7 0 0 0-7 7c0 5 7 13 7 13s7-8 7-13a7 7 0 0 0-7-7zm0 9.5A2.5 2.5 0 1 1 12 6.5a2.5 2.5 0 0 1 0 5z"/></svg></span>
    <div>123 Building Name, Street Name,<br>City Name, State XY-123456</div>
  </div>
  <div class="vsep" style="left:507px"></div>
  <div class="contact" style="left:554px">
    <span class="ic"><svg width="18" height="18" viewBox="0 0 24 24" fill="#253a6c"><path d="M6.6 10.8a15 15 0 0 0 6.6 6.6l2.2-2.2a1 1 0 0 1 1-.25 11.4 11.4 0 0 0 3.6.57 1 1 0 0 1 1 1V20a1 1 0 0 1-1 1A17 17 0 0 1 3 4a1 1 0 0 1 1-1h3.5a1 1 0 0 1 1 1c0 1.25.2 2.45.57 3.6a1 1 0 0 1-.25 1z"/></svg></span>
    <div>Phone<br>123 456 7890</div>
  </div>
  <div class="vsep" style="left:750px"></div>
  <div class="contact" style="left:795px">
    <span class="ic"><svg width="18" height="18" viewBox="0 0 24 24" fill="#253a6c"><path d="M3 5h18v14H3z"/><path d="M3 6l9 7 9-7" stroke="#fff" stroke-width="1.6" fill="none"/></svg></span>
    <div>E-mail<br>info@meadowlarkcrest.com</div>
  </div>
  <div class="copyright">© 2024 Meadowlark Crest Nutraceutical . All Rights Reserved.</div>
  <span class="social" style="left:943px"></span>
  <span class="social" style="left:972px"></span>
  <span class="social" style="left:1002px"></span>
  <span class="social" style="left:1034px"></span>
</footer>

<section class="job">
  <div class="job-photo" role="img" aria-label="Man working on a laptop at a desk"></div>
  <h2>Job Applications</h2>
  <p>Lorem ipsum dolor sit amet, consectetur adipiscing elit. Mauris at ante quis nunc faucibus ullamcorper sed eget ipsum vitae augue aliquet.</p>
  <div class="btn btn-navy" style="left:30px;top:182px;width:140px;height:33px">Enquire Here</div>
  <div class="job-candy" role="img" aria-label="Pile of colourful gummies"></div>
</section>

</body>
</html>
```